IT’S NOT A CLEANING, IT’S YOUR LIFE! TOP TEN REASONS WHY THIS IS NOT JUST A “CLEANING”

We made a list for our patients to let them know why our hygiene appointments are different than other cleanings. Since this is a lot of information, we would like it easily readable within 4-5 feet but we do not want the post to be HUGE. Please see below:

IT’S NOT A CLEANING, IT’S YOUR LIFE!
TOP TEN REASONS WHY THIS IS NOT JUST A “CLEANING”

10. We make you look better. Healthy teeth and gums are more attractive. Recent studies
show that the smile is the first thing people notice and that people with better looking teeth
are more confident and successful.

9. We can relieve your headaches. During your hygiene visit we evaluate for serious bite
issues, many of which lead to muscle soreness, headaches, and migraines.

8. We check for oral cancer. Oral cancer kills 1 person per hour 24 hours a day. The death rate for oral cancer is higher than cancers we routinely hear about such as cervical, thyroid and skin cancer.

7. We make you smell better. During your hygiene visit we eliminate many of the germs that live under your gum tissue and cause bad breath.

6. We save you money. By utilizing the latest dental technology (digital x-rays, mouth
cameras, and magnification glasses) we can help with early detection of tooth and gum
problems and save you the cost of gum surgery, root canals, and implants.

5. We clean in places you cannot. We clean under the gum line and between teeth where
most of the germs hide and cause dental disease. 40% of the bacteria in your mouth lives in
between your teeth.

4. We prevent pain. We identify tooth decay that can lead to nerve involvement and pain,
root canal, and tooth loss.

3. We save your teeth. Most tooth loss is from periodontal/gum disease. At each visit we
evaluate the health of your gums and bone with our periodontal screening. Periodontal
disease, like high blood pressure, is symptomless until it is in advanced stages.

2. We protect your loved ones. Studies have proven that the bacteria that cause dental
disease can be transmitted from person to person. Think about that the next time you kiss
someone!

1. We prolong life. Researchers have linked the inflammation and infection found in the
mouth to heart attacks, strokes, and Alzheimer’s. By reducing infection in your mouth we can
greatly improve your overall health!

```html
<!DOCTYPE html>
<html lang="en">
<head>
<meta charset="utf-8">
<title>It's Not a Cleaning. It's Your Life!</title>
<link rel="stylesheet" href="https://fonts.googleapis.com/css2?family=Oswald:wght@300;400;600;700&family=Roboto:wght@400;500&family=Caveat:wght@500;700&display=swap">
<style>
  :root {
    --ink: #0b0b0b;
    --paper: #ffffff;
    --text: #111111;
  }
  html, body {
    margin: 0;
    padding: 0;
    overflow: hidden;
    background: var(--paper);
  }
  .poster {
    position: relative;
    width: 927px;
    height: 1200px;
    background: var(--paper);
    overflow: hidden;
  }
  .banner {
    position: absolute;
    left: 21px; top: 21px;
    width: 885px; height: 79px;
    background: var(--ink);
    color: var(--paper);
    display: flex;
    align-items: center;
    justify-content: center;
    font-family: "Oswald", sans-serif;
    font-weight: 300;
    font-size: 46px;
    letter-spacing: 0.5px;
    white-space: nowrap;
  }
  .banner strong { font-weight: 600; margin-left: 12px; }
  .board {
    position: absolute;
    left: 21px; top: 118px;
    width: 885px; height: 1061px;
    background: var(--ink);
  }
  .title {
    position: absolute;
    left: 330px; top: 133px;
    width: 564px; height: 164px;
    color: var(--paper);
    font-family: "Oswald", sans-serif;
  }
  .title-top {
    position: absolute;
    left: 6px; top: 4px;
    white-space: nowrap;
  }
  .title-big {
    font-weight: 700;
    font-size: 48px;
    line-height: 1;
  }
  .title-small {
    font-weight: 400;
    font-size: 27px;
    margin-left: 10px;
  }
  .title-just {
    position: absolute;
    left: 40px; top: 52px;
    font-family: "Caveat", cursive;
    font-weight: 500;
    font-size: 70px;
    line-height: 1;
  }
  .title-cleaning {
    position: absolute;
    left: 185px; top: 60px;
    font-weight: 700;
    font-size: 44px;
    line-height: 1;
    white-space: nowrap;
  }
  .reason {
    position: absolute;
    box-sizing: border-box;
    background: var(--paper);
    padding: 12px 12px 10px 14px;
    color: var(--text);
  }
  .reason-head {
    display: flex;
    align-items: flex-start;
    gap: 8px;
    margin-bottom: 4px;
  }
  .reason-num {
    font-family: "Caveat", cursive;
    font-weight: 700;
    font-size: 66px;
    line-height: 0.8;
    flex: none;
  }
  .reason-title {
    font-family: "Oswald", sans-serif;
    font-weight: 400;
    font-size: 23px;
    line-height: 1.15;
    margin: 0;
    padding-top: 2px;
  }
  .reason-text {
    font-family: "Roboto", sans-serif;
    font-weight: 500;
    font-size: 14.6px;
    line-height: 1.36;
    margin: 0;
  }
  .reason-text.indent { text-indent: 30px; }

  .r10 { left: 39px;  top: 133px; width: 279px; height: 285px; }
  .r7  { left: 39px;  top: 435px; width: 279px; height: 186px; }
  .r4  { left: 39px;  top: 638px; width: 279px; height: 195px; }
  .r3  { left: 39px;  top: 850px; width: 279px; height: 317px; }
  .r9  { left: 330px; top: 342px; width: 278px; height: 173px; }
  .r6  { left: 330px; top: 530px; width: 278px; height: 311px; }
  .r2  { left: 330px; top: 848px; width: 278px; height: 319px; }
  .r8  { left: 617px; top: 297px; width: 277px; height: 279px; }
  .r5  { left: 617px; top: 591px; width: 277px; height: 242px; }
  .r1  { left: 617px; top: 848px; width: 277px; height: 319px; }
</style>
</head>
<body>
<main class="poster">
  <header class="banner">IT’S NOT A CLEANING. <strong>IT’S YOUR LIFE!</strong></header>

  <div class="board"></div>

  <h1 class="title">
    <span class="title-top"><span class="title-big">TOP TEN</span><span class="title-small">REASONS WHY THIS IS NOT</span></span>
    <span class="title-just">Just</span>
    <span class="title-cleaning">A “CLEANING”</span>
  </h1>

  <section class="reason r10">
    <div class="reason-head"><span class="reason-num">10.</span><h2 class="reason-title">We make you<br>look better.</h2></div>
    <p class="reason-text">Healthy teeth and gums are more attractive. Recent studies show that the smile is the first thing people notice and that people with better looking teeth are more confident and successful.</p>
  </section>

  <section class="reason r7">
    <div class="reason-head"><span class="reason-num">7.</span><h2 class="reason-title">We make you<br>smell better.</h2></div>
    <p class="reason-text indent">During your hygiene visit we eliminate many of the germs that live under your gum tissue and cause bad breath.</p>
  </section>

  <section class="reason r4">
    <div class="reason-head"><span class="reason-num">4.</span><h2 class="reason-title">We prevent<br>pain.</h2></div>
    <p class="reason-text">We identify tooth decay that can lead to nerve involvement and pain, root canal, and tooth loss.</p>
  </section>

  <section class="reason r3">
    <div class="reason-head"><span class="reason-num">3.</span><h2 class="reason-title">We save your<br>teeth.</h2></div>
    <p class="reason-text">Most tooth loss is from periodontal/gum disease. At each visit we evaluate the health of your gums and bone with our periodontal screening. Periodontal disease, like high blood pressure, is symptomless until it is in advanced stages.</p>
  </section>

  <section class="reason r9">
    <div class="reason-head"><span class="reason-num">9.</span><h2 class="reason-title">We can relieve<br>your headaches.</h2></div>
    <p class="reason-text indent">During your hygiene visit we evaluate for serious bite issues, many of which lead to muscle soreness, headaches, and migraines.</p>
  </section>

  <section class="reason r6">
    <div class="reason-head"><span class="reason-num">6.</span><h2 class="reason-title">We save you<br>money.</h2></div>
    <p class="reason-text indent">By utilizing the latest dental technology (digital x-rays, mouth cameras, and magnification glasses) we can help with early detection of tooth and gum problems and save you the cost of gum surgery, root canals, and implants.</p>
  </section>

  <section class="reason r2">
    <div class="reason-head"><span class="reason-num">2.</span><h2 class="reason-title">We protect your<br>loved ones.</h2></div>
    <p class="reason-text">Studies have proven that the bacteria that cause dental disease can be transmitted from person to person. Think about that the next time you kiss someone!</p>
  </section>

  <section class="reason r8">
    <div class="reason-head"><span class="reason-num">8.</span><h2 class="reason-title">We check for<br>oral cancer.</h2></div>
    <p class="reason-text indent">Oral cancer kills 1 person per hour 24 hours a day. The death rate for oral cancer is higher than cancers we routinely hear about such as cervical, thyroid and skin cancer.</p>
  </section>

  <section class="reason r5">
    <div class="reason-head"><span class="reason-num">5.</span><h2 class="reason-title">We clean in<br>places you<br>cannot.</h2></div>
    <p class="reason-text">We clean under the gum line and between teeth where most of the germs hide and cause dental disease. 40% of the bacteria in your mouth lives in between your teeth.</p>
  </section>

  <section class="reason r1">
    <div class="reason-head"><span class="reason-num">1.</span><h2 class="reason-title">We prolong life.</h2></div>
    <p class="reason-text indent">Researchers have linked the inflammation and infection found in the mouth to heart attacks, strokes, and Alzheimer’s. By reducing infection in your mouth we can greatly improve your overall health!</p>
  </section>
</main>
</body>
</html>
```